Flyer-Design für psychologisches Coaching  und Taiji
Flyer-Design für psychologisches Coaching und Taiji
Zielgruppe
Seit Januar 2020 habe ich mich selbständig gemacht und biete unter dem Namen 'WANDELRAUM - Mara Brenner, Coaching und Bewegung' Coaching sowie Taiji an. Der Corona-Lockdown hat meinen Geschäftseintritt stark beeinflusst, so dass ich für den Restart einen professionellen Flyer benötige, um mich und mein Angebot bekannt zu machen. Die Flyer werde ich vor meinen Räumen sowie in Geschäften im Umkreis und/oder per Einwurf verteilen.
Meine Zielgruppe sind gesundheitsorientierte Menschen in der zweiten Lebenshälfte, die ihre Balance finden wollen.
Mehr im separaten Dokument, bitte lesen.
Aufgabenstellung
Das Design soll zum Logo und zu meinem angestrebten Image passen. Ich möchte seriös, sympathisch und authentisch rüberkommen. Das psychologische Coaching und Taiji sollen gleichwertig und harmonisch präsentiert werden. Die Texte sollen kurz und prägnant sein. Textvorschläge gebe ich im Briefing und freue mich über neue, aussagefähige Formulierungen.
Mehr im beigefügten Dokument, bitte lesen.

```html
<!DOCTYPE html>
<html lang="de">
<head>
<meta charset="utf-8">
<title>WANDELRAUM – Flyer Innenseite</title>
<link rel="stylesheet" href="https://fonts.googleapis.com/css2?family=Open+Sans:wght@700;800&family=Ubuntu:wght@400;500;700&display=swap">
<style>
  :root {
    --olive-dark: #a6992f;
    --olive-mid: #bcb036;
    --olive-light: #d8cb3b;
    --olive-text: #a99b2c;
    --figure-tone: #d7d3a8;
    --ink: #2b2b2b;
    --paper: #ffffff;
  }
  * { margin: 0; padding: 0; box-sizing: border-box; }
  html, body {
    width: 869px; height: 1200px; overflow: hidden;
    background: var(--paper);
    font-family: "Ubuntu", sans-serif;
    color: var(--ink);
  }
  .canvas { position: relative; width: 869px; height: 1200px; overflow: hidden; }

  .flyer { position: absolute; left: 0; width: 869px; height: 614px; }
  .flyer--first { top: 0; }
  .flyer--second { top: 580px; }

  .hero-strip { position: absolute; left: 0; top: 0; width: 869px; height: 82px; }
  .header-band { position: absolute; left: 0; top: 60px; width: 869px; height: 92px; }
  .footer-band { position: absolute; left: 0; top: 574px; width: 869px; height: 40px; }

  .section-title {
    position: absolute;
    font-family: "Open Sans", sans-serif;
    font-weight: 800;
    font-size: 18px;
    line-height: 21.5px;
    letter-spacing: 0.4px;
    color: var(--paper);
    text-transform: uppercase;
    white-space: nowrap;
  }
  .section-title--coaching { left: 24px; top: 84px; }
  .section-title--taiji { left: 309px; top: 85px; }
  .section-title--meditation { left: 601px; top: 85px; }

  .column {
    position: absolute; top: 161px;
    font-size: 9.1px; line-height: 12.4px;
    white-space: nowrap;
  }
  .column--coaching { left: 25px; width: 240px; }
  .column--taiji { left: 309px; width: 270px; }
  .column--meditation { left: 601px; width: 262px; }

  .lead-heading {
    font-weight: 500; font-size: 10.8px; line-height: 14.8px;
    color: var(--olive-text); margin-bottom: 4px;
  }
  .sub-heading {
    font-weight: 500; font-size: 10.8px; line-height: 14px;
    color: var(--olive-text); margin: 11px 0 5px;
  }
  .bullets { list-style: none; }
  .bullets li { position: relative; padding-left: 7.5px; }
  .bullets li::before { content: "•"; position: absolute; left: 0; }
  .bullets--spaced li + li { margin-top: 7px; }
  .column p + p { margin-top: 12.4px; }

  .contact {
    position: absolute; left: 25px; top: 480px;
    font-size: 9.1px; line-height: 12.4px; white-space: nowrap;
  }
  .contact .sub-heading { margin: 0 0 7px; }

  .photo { position: absolute; }
</style>
</head>
<body>
<main class="canvas">

  <section class="flyer flyer--first">
    <svg class="hero-strip" viewBox="0 0 869 82" role="img" aria-label="Foto: Hände bei Taiji-Bewegungen vor hellem, warmem Hintergrund">
      <defs>
        <linearGradient id="heroGlow" x1="0" y1="0" x2="1" y2="0">
          <stop offset="0" stop-color="#d9d4cc"/>
          <stop offset="0.3" stop-color="#f3c9a4"/>
          <stop offset="0.55" stop-color="#f5e6c0"/>
          <stop offset="0.8" stop-color="#eef0e6"/>
          <stop offset="1" stop-color="#e4ddd2"/>
        </linearGradient>
      </defs>
      <path d="M0 0 H869 V52 C700 58 520 64 300 70 C180 72 80 76 0 78 Z" fill="url(#heroGlow)"/>
    </svg>

    <svg class="header-band" viewBox="0 0 869 92" aria-hidden="true">
      <path d="M0 12 L294 8 L294 66 L0 84 Z" fill="var(--olive-dark)"/>
      <path d="M293 8 L587 4 L587 60 L293 68 Z" fill="var(--olive-mid)"/>
      <path d="M586 4 L869 1 L869 56 L586 61 Z" fill="var(--olive-light)"/>
      <path d="M0 82 C200 72 500 64 869 56" stroke="var(--olive-dark)" stroke-width="2" fill="none" opacity="0.6"/>
    </svg>

    <h2 class="section-title section-title--coaching">Psychologisches<br>Coaching</h2>
    <h2 class="section-title section-title--taiji">Taiji und Qigong</h2>
    <h2 class="section-title section-title--meditation">Meditation</h2>

    <svg class="photo" style="left:455px;top:381px" width="206" height="211" viewBox="0 0 206 211" role="img" aria-label="Bildfläche für eine Silhouette einer meditierenden Person im Lotussitz">
      <defs>
        <linearGradient id="figureFade1" x1="0" y1="0" x2="0" y2="1">
          <stop offset="0" stop-color="var(--figure-tone)" stop-opacity="0.35"/>
          <stop offset="1" stop-color="var(--figure-tone)"/>
        </linearGradient>
      </defs>
      <rect x="0" y="0" width="206" height="211" rx="14" fill="url(#figureFade1)"/>
    </svg>

    <div class="column column--coaching">
      <h3 class="lead-heading">Holen Sie sich Begleitung über einen zeitlich<br>begrenzten Zeitraum in einer Situation, die<br>Sie selbst als schwierig empfinden</h3>
      <ul class="bullets bullets--spaced">
        <li>Persönlichen Krisensituation wie einer Trennung,<br>einem Konflikt, dem (drohenden) Verlust des<br>Arbeitsplatzes oder der Pflege von Angehörigen</li>
        <li>Sie möchten sich privat oder beruflich neu orientieren<br>und suchen jemanden, die Ihnen hilft, Ihren ganz<br>persönlichen Weg zu finden</li>
        <li>Sie möchten Ihr Leben entschleunigen, um sich<br>vor Erschöpfung und Burn-out zu schützen</li>
      </ul>
      <h3 class="sub-heading">Das biete ich Ihnen</h3>
      <ul class="bullets bullets--spaced">
        <li>Ich bin Ihre Wegbegleiterin auf Zeit, die ihre eigene<br>Lebens- und Berufserfahrung als Führungskraft</li>
        <li>Wichtig ist für mich, dass Sie aus dem Coaching einen<br>nachhaltigen Nutzen ziehen. Dieser kann zum Beispiel<br>eine veränderte Einstellung sein, die Ihnen mehr<br>Spielraum gibt.</li>
      </ul>
    </div>

    <div class="contact">
      <h3 class="sub-heading">Gerne bin ich für Sie da</h3>
      <p>Vereinbaren Sie unverbindlich<br>ein kostenloses Erstgespräch<br>mit mir entweder per Mail<br>unter info@wandelraum.de<br>oder telefonisch unter<br>0151 234 56 70.</p>
    </div>

    <svg class="photo" style="left:168px;top:484px" width="102" height="102" viewBox="0 0 102 102" role="img" aria-label="Porträtfoto von Mara Brenner">
      <circle cx="51" cy="51" r="49" fill="none" stroke="var(--olive-dark)" stroke-width="3"/>
      <circle cx="51" cy="51" r="45" fill="#8e2a28"/>
    </svg>

    <div class="column column--taiji">
      <p>Taiji und Qigong sind langsame und fließende Bewegungen.<br>Beides stammt aus den Kampfkünsten im alten China und dient<br>der Gesundheitsförderung. Ich unterrichte nach der Tradition<br>der Familie Shen. Die Teilnehmenden richten Ihre Aufmerksam-<br>keit nach innen bzw. ganz auf die Bewegungen.</p>
      <h3 class="sub-heading">Möglicher Nutzen für Sie</h3>
      <ul class="bullets">
        <li>Mehr Ruhe und Gelassenheit im Alltag</li>
        <li>Schulung der Konzentration</li>
        <li>Verbesserung der Körperwahrnehmung</li>
        <li>Kräftigung der Sehnen und Gelenke</li>
        <li>Aufrechtere Körperhaltung</li>
      </ul>
      <h3 class="sub-heading">Wie können Sie einsteigen?</h3>
      <p>Bitte besuchen Sie immer zuerst eine kostenlose<br>Schnupperstunde bei mir, um Taiji und Qigong<br>einfach mal auszuprobieren. Bitte seien sie<br>mindestens 10 min vor Beginn der Stunde da,<br>um sich entsprechend einstimmen zu können.<br>Tragen Sie bequeme Sportkleidung und warme<br>Socken oder Taiji-Schuhe. Auch Stoppersocken<br>oder Barfußschuhe sind okay.</p>
    </div>

    <svg class="photo" style="left:305px;top:470px" width="96" height="96" viewBox="0 0 96 96" role="img" aria-label="Foto: Frau in weißer Kleidung übt Taiji im Park">
      <circle cx="48" cy="48" r="46" fill="none" stroke="var(--olive-dark)" stroke-width="3"/>
      <circle cx="48" cy="48" r="42" fill="#6c7466"/>
    </svg>
    <svg class="photo" style="left:387px;top:511px" width="78" height="78" viewBox="0 0 78 78" role="img" aria-label="Foto: Hand in weißem Ärmel bei einer Taiji-Bewegung">
      <circle cx="39" cy="39" r="37" fill="none" stroke="var(--olive-dark)" stroke-width="3"/>
      <circle cx="39" cy="39" r="33" fill="#8a8f86"/>
    </svg>

    <div class="column column--meditation">
      <p>Kennen Sie das? Sie haben noch 1000 Dinge auf Ihrer<br>to-do-Liste und wissen nicht, wo Ihnen der Kopf steht.<br>Und Sie wissen, dass Sie endlich mal was für sich tun<br>sollten. Aber wann den bloß?</p>
      <p>Für mehr und mehr Menschen ist es wichtig, im<br>hektischen Alltag Inseln der Ruhe zu schaffen. Andere<br>wiederum können es sich kaum vorstellen, mehrere<br>Minuten lang still zu sitzen. Und dann auch noch zu<br>schweigen. Unvorstellbar!</p>
      <h3 class="sub-heading">Offener Meditationsabend einmal im Monat</h3>
      <p>Falls Sie es ausprobieren möchten oder eine regelmäßige<br>Meditationsgruppe suchen, kommen Sie doch einfach<br>zu einem meiner offenen Meditationsabende. Jede/r ist<br>herzlich eingeladen. Wir erkunden unter meiner Anleitung<br>verschiedenen Techniken aus verschiedenen Meditations-<br>praktiken frei von religiöser oder spiritueller Bindung. Diese<br>Abende biete ich auf der Basis freiwilliger Kostenbeteiligung<br>an. Die Termine finden Sie auf dem Terminblatt oder auf<br>meiner Website.</p>
    </div>

    <svg class="photo" style="left:716px;top:440px" width="110" height="110" viewBox="0 0 110 110" role="img" aria-label="Foto: Mara Brenner sitzt meditierend vor einem gemalten Hintergrund">
      <circle cx="55" cy="55" r="53" fill="none" stroke="var(--olive-dark)" stroke-width="3"/>
      <circle cx="55" cy="55" r="49" fill="#5b5a5e"/>
    </svg>
    <svg class="photo" style="left:660px;top:496px" width="86" height="86" viewBox="0 0 86 86" role="img" aria-label="Foto: Mara Brenner mit erhobenen Armen bei einer Qigong-Übung">
      <circle cx="43" cy="43" r="41" fill="none" stroke="var(--olive-dark)" stroke-width="3"/>
      <circle cx="43" cy="43" r="37" fill="#8a8579"/>
    </svg>

    <svg class="footer-band" viewBox="0 0 869 40" aria-hidden="true">
      <defs>
        <linearGradient id="footGrad" x1="0" y1="0" x2="1" y2="0">
          <stop offset="0" stop-color="var(--olive-mid)"/>
          <stop offset="1" stop-color="var(--olive-dark)"/>
        </linearGradient>
      </defs>
      <path d="M0 20 C250 17 560 14 869 4 V40 H0 Z" fill="url(#footGrad)"/>
    </svg>
  </section>

  <section class="flyer flyer--second">
    <svg class="header-band" viewBox="0 0 869 92" aria-hidden="true">
      <path d="M0 12 L294 8 L294 66 L0 84 Z" fill="var(--olive-dark)"/>
      <path d="M293 8 L587 4 L587 60 L293 68 Z" fill="var(--olive-mid)"/>
      <path d="M586 4 L869 1 L869 56 L586 61 Z" fill="var(--olive-light)"/>
      <path d="M0 82 C200 72 500 64 869 56" stroke="var(--olive-dark)" stroke-width="2" fill="none" opacity="0.6"/>
    </svg>

    <h2 class="section-title section-title--coaching">Psychologisches<br>Coaching</h2>
    <h2 class="section-title section-title--taiji">Taiji und Qigong</h2>
    <h2 class="section-title section-title--meditation">Meditation</h2>

    <svg class="photo" style="left:455px;top:411px" width="206" height="211" viewBox="0 0 206 211" role="img" aria-label="Bildfläche für eine Silhouette einer meditierenden Person im Lotussitz">
      <defs>
        <linearGradient id="figureFade2" x1="0" y1="0" x2="0" y2="1">
          <stop offset="0" stop-color="var(--figure-tone)" stop-opacity="0.35"/>
          <stop offset="1" stop-color="var(--figure-tone)"/>
        </linearGradient>
      </defs>
      <rect x="0" y="0" width="206" height="211" rx="14" fill="url(#figureFade2)"/>
    </svg>

    <div class="column column--coaching">
      <h3 class="lead-heading">Holen Sie sich Begleitung über einen zeitlich<br>begrenzten Zeitraum in einer Situation, die<br>Sie selbst als schwierig empfinden</h3>
      <ul class="bullets bullets--spaced">
        <li>Persönlichen Krisensituation wie einer Trennung,<br>einem Konflikt, dem (drohenden) Verlust des<br>Arbeitsplatzes oder der Pflege von Angehörigen</li>
        <li>Sie möchten sich privat oder beruflich neu orientieren<br>und suchen jemanden, die Ihnen hilft, Ihren ganz<br>persönlichen Weg zu finden</li>
        <li>Sie möchten Ihr Leben entschleunigen, um sich<br>vor Erschöpfung und Burn-out zu schützen</li>
      </ul>
      <h3 class="sub-heading">Das biete ich Ihnen</h3>
      <ul class="bullets bullets--spaced">
        <li>Ich bin Ihre Wegbegleiterin auf Zeit, die ihre eigene<br>Lebens- und Berufserfahrung als Führungskraft</li>
        <li>Wichtig ist für mich, dass Sie aus dem Coaching einen<br>nachhaltigen Nutzen ziehen. Dieser kann zum Beispiel<br>eine veränderte Einstellung sein, die Ihnen mehr<br>Spielraum gibt.</li>
      </ul>
    </div>

    <div class="contact">
      <h3 class="sub-heading">Gerne bin ich für Sie da</h3>
      <p>Vereinbaren Sie unverbindlich<br>ein kostenloses Erstgespräch<br>mit mir entweder per Mail<br>unter info@wandelraum.de<br>oder telefonisch unter<br>0151 234 56 70.</p>
    </div>

    <svg class="photo" style="left:168px;top:516px" width="102" height="102" viewBox="0 0 102 102" role="img" aria-label="Porträtfoto von Mara Brenner">
      <circle cx="51" cy="51" r="49" fill="none" stroke="var(--olive-dark)" stroke-width="3"/>
      <circle cx="51" cy="51" r="45" fill="#8e2a28"/>
    </svg>

    <div class="column column--taiji">
      <p>Taiji und Qigong sind langsame und fließende Bewegungen.<br>Beides stammt aus den Kampfkünsten im alten China und dient<br>der Gesundheitsförderung. Ich unterrichte nach der Tradition<br>der Familie Shen. Die Teilnehmenden richten Ihre Aufmerksam-<br>keit nach innen bzw. ganz auf die Bewegungen.</p>
      <h3 class="sub-heading">Möglicher Nutzen für Sie</h3>
      <ul class="bullets">
        <li>Mehr Ruhe und Gelassenheit im Alltag</li>
        <li>Schulung der Konzentration</li>
        <li>Verbesserung der Körperwahrnehmung</li>
        <li>Kräftigung der Sehnen und Gelenke</li>
        <li>Aufrechtere Körperhaltung</li>
      </ul>
      <h3 class="sub-heading">Wie können Sie einsteigen?</h3>
      <p>Bitte besuchen Sie immer zuerst eine kostenlose<br>Schnupperstunde bei mir, um Taiji und Qigong<br>einfach mal auszuprobieren. Bitte seien sie<br>mindestens 10 min vor Beginn der Stunde da,<br>um sich entsprechend einstimmen zu können.<br>Tragen Sie bequeme Sportkleidung und warme<br>Socken oder Taiji-Schuhe. Auch Stoppersocken<br>oder Barfußschuhe sind okay.</p>
    </div>

    <svg class="photo" style="left:305px;top:490px" width="96" height="96" viewBox="0 0 96 96" role="img" aria-label="Foto: Frau in weißer Kleidung übt Taiji im Park">
      <circle cx="48" cy="48" r="46" fill="none" stroke="var(--olive-dark)" stroke-width="3"/>
      <circle cx="48" cy="48" r="42" fill="#6c7466"/>
    </svg>
    <svg class="photo" style="left:387px;top:531px" width="78" height="78" viewBox="0 0 78 78" role="img" aria-label="Foto: Hand in weißem Ärmel bei einer Taiji-Bewegung">
      <circle cx="39" cy="39" r="37" fill="none" stroke="var(--olive-dark)" stroke-width="3"/>
      <circle cx="39" cy="39" r="33" fill="#8a8f86"/>
    </svg>

    <div class="column column--meditation">
      <p>Kennen Sie das? Sie haben noch 1000 Dinge auf Ihrer<br>to-do-Liste und wissen nicht, wo Ihnen der Kopf steht.<br>Und Sie wissen, dass Sie endlich mal was für sich tun<br>sollten. Aber wann den bloß?</p>
      <p>Für mehr und mehr Menschen ist es wichtig, im<br>hektischen Alltag Inseln der Ruhe zu schaffen. Andere<br>wiederum können es sich kaum vorstellen, mehrere<br>Minuten lang still zu sitzen. Und dann auch noch zu<br>schweigen. Unvorstellbar!</p>
      <h3 class="sub-heading">Offener Meditationsabend einmal im Monat</h3>
      <p>Falls Sie es ausprobieren möchten oder eine regelmäßige<br>Meditationsgruppe suchen, kommen Sie doch einfach<br>zu einem meiner offenen Meditationsabende. Jede/r ist<br>herzlich eingeladen. Wir erkunden unter meiner Anleitung<br>verschiedenen Techniken aus verschiedenen Meditations-<br>praktiken frei von religiöser oder spiritueller Bindung. Diese<br>Abende biete ich auf der Basis freiwilliger Kostenbeteiligung<br>an. Die Termine finden Sie auf dem Terminblatt oder auf<br>meiner Website.</p>
    </div>

    <svg class="photo" style="left:716px;top:472px" width="110" height="110" viewBox="0 0 110 110" role="img" aria-label="Foto: Mara Brenner sitzt meditierend vor einem gemalten Hintergrund">
      <circle cx="55" cy="55" r="53" fill="none" stroke="var(--olive-dark)" stroke-width="3"/>
      <circle cx="55" cy="55" r="49" fill="#5b5a5e"/>
    </svg>
    <svg class="photo" style="left:660px;top:528px" width="86" height="86" viewBox="0 0 86 86" role="img" aria-label="Foto: Mara Brenner mit erhobenen Armen bei einer Qigong-Übung">
      <circle cx="43" cy="43" r="41" fill="none" stroke="var(--olive-dark)" stroke-width="3"/>
      <circle cx="43" cy="43" r="37" fill="#8a8579"/>
    </svg>
  </section>

</main>
</body>
</html>
```